Hearth of the Heron: Half-Page Magazine Ad

advertisement in a travel magazine for a casual/fine dining restaurant in the heart of Whitehorse, Yukon
Needs to say that it is located in the Stonereach Hotel, 247 Larch Avenue.

Northern inspired cuisine
hearthoftheheron-example.ca

Don't need to use all the pictures

Dimensions: ad is a half-page, dimensions are 7.25" x 4.8".

Target Market(s)

Upscale dining, corporate travellers

Industry/Entity Type

Restaurant

Colors
0054AA
0677BA
7BADD7
CADEEF
E8F1F8
0094D4
00A9DD
6FCCEA
C7EBF8
E9F6FB
00AB8E
00BBA5
67D7C9
C6EFE9
E9F9F6

Requirements
Must have
• Restaurant logo
Nice to have
• Simple, clean design with upscale feel

```html
<!DOCTYPE html>
<html lang="en">
<head>
<meta charset="utf-8">
<title>Hearth of the Heron – Half-Page Ad</title>
<link href="https://fonts.googleapis.com/css2?family=Montserrat:ital,wght@0,400;0,500;0,600;0,700;1,700&family=Yellowtail&family=Kaushan+Script&display=block" rel="stylesheet">
<style>
  :root {
    --page: #b9b9b9;
    --ink-dark: #161616;
    --paper: #ffffff;
    --logo-ink: #2b2b2b;
    --motif-tone: #3a3a3a;
  }
  html, body {
    margin: 0;
    width: 890px;
    height: 1200px;
    overflow: hidden;
    background: var(--page);
    font-family: "Montserrat", Arial, sans-serif;
  }
  .ad {
    position: absolute;
    left: 20px;
    top: 316px;
    width: 850px;
    height: 567px;
    overflow: hidden;
    box-shadow: -6px 6px 8px rgba(0,0,0,.45);
    color: var(--paper);
  }
  .ad-art { position: absolute; inset: 0; }
  .logo {
    position: absolute;
    left: 42px;
    top: 52px;
    display: flex;
    align-items: center;
    gap: 16px;
    color: var(--logo-ink);
    font-weight: 700;
    text-transform: uppercase;
  }
  .logo-mark {
    width: 74px; height: 74px;
    border-radius: 50%;
    background: var(--logo-ink);
    flex: none;
  }
  .logo-name { font-size: 25px; line-height: 1.08; letter-spacing: 1px; }
  .headline {
    position: absolute;
    right: 38px;
    top: 22px;
    margin: 0;
    font-family: "Yellowtail", "Kaushan Script", cursive;
    font-weight: 400;
    font-size: 58px;
    line-height: 1.2;
    white-space: nowrap;
  }
  .intro {
    position: absolute;
    right: 25px;
    top: 119px;
    margin: 0;
    text-align: right;
    font-size: 16.3px;
    font-weight: 500;
    line-height: 21.5px;
  }
  .features {
    position: absolute;
    right: 34px;
    top: 215px;
    margin: 0;
    padding: 0;
    list-style: none;
  }
  .feature {
    display: flex;
    justify-content: flex-end;
    align-items: flex-start;
    gap: 16px;
    margin-bottom: 22px;
    text-align: right;
    font-style: italic;
    font-weight: 700;
    font-size: 17px;
    line-height: 21.5px;
  }
  .feature svg { flex: none; margin-top: 3px; }
  .contact-label {
    position: absolute;
    right: 25px;
    top: 367px;
    margin: 0;
    font-size: 14px;
    font-weight: 500;
    letter-spacing: 3.2px;
  }
  .phone {
    position: absolute;
    right: 23px;
    top: 394px;
    margin: 0;
    font-size: 37px;
    font-weight: 700;
    letter-spacing: -0.5px;
  }
  .location {
    position: absolute;
    left: 505px;
    top: 450px;
    width: 318px;
    height: 90px;
    border: 1.5px solid var(--paper);
    box-sizing: border-box;
  }
  .location-tab {
    position: absolute;
    right: 0; top: 0;
    width: 130px; height: 24px;
    background: var(--paper);
    color: var(--ink-dark);
    clip-path: polygon(0 0, 100% 0, 100% 100%, 14% 100%);
    font-size: 10.5px;
    font-weight: 500;
    line-height: 24px;
    text-align: right;
    padding-right: 8px;
    box-sizing: border-box;
  }
  .address {
    position: absolute;
    right: 8px; top: 34px;
    margin: 0;
    font-size: 14.6px;
    font-weight: 700;
    white-space: nowrap;
  }
  .website {
    position: absolute;
    right: 8px; top: 62px;
    margin: 0;
    font-size: 10px;
    letter-spacing: 1.8px;
  }
</style>
</head>
<body>
<section class="ad" aria-label="Hearth of the Heron half-page advertisement">
  <svg class="ad-art" viewBox="0 0 850 567" width="850" height="567">
    <defs>
      <linearGradient id="interiorTone" x1="0" y1="0" x2="1" y2="1">
        <stop offset="0" stop-color="#202020"/>
        <stop offset=".6" stop-color="#141414"/>
        <stop offset="1" stop-color="#1c1c1c"/>
      </linearGradient>
      <radialGradient id="pastaTone" cx=".5" cy=".45" r=".6">
        <stop offset="0" stop-color="#7a8f3a"/>
        <stop offset="1" stop-color="#a8743a"/>
      </radialGradient>
      <radialGradient id="steakTone" cx=".5" cy=".45" r=".6">
        <stop offset="0" stop-color="#c9bd9a"/>
        <stop offset="1" stop-color="#6e4a3a"/>
      </radialGradient>
      <radialGradient id="boardTone" cx=".55" cy=".5" r=".6">
        <stop offset="0" stop-color="#d9a84a"/>
        <stop offset="1" stop-color="#8c3b34"/>
      </radialGradient>
    </defs>

    <rect class="interior-photo" width="850" height="567" fill="url(#interiorTone)" role="img" aria-label="Dim photograph of the restaurant dining room"/>

    <path class="logo-panel" fill="#ffffff"
      d="M0 0 H311 C338 40 348 118 337 152 C326 190 300 206 268 209 C205 213 160 210 118 232 C62 262 22 292 0 322 Z"/>

    <rect class="ornament-area" x="0" y="462" width="64" height="105" fill="#2e2e2e" role="img" aria-label="Decorative line ornament in the corner"/>
    <rect class="ornament-area" x="420" y="202" width="44" height="44" fill="#2e2e2e" role="img" aria-label="Small decorative ornament"/>
    <rect class="ornament-area" x="206" y="518" width="80" height="26" fill="#2e2e2e" role="img" aria-label="Decorative wave ornament"/>
    <rect class="ornament-area" x="333" y="462" width="92" height="24" fill="#2e2e2e" role="img" aria-label="Decorative dot pattern"/>

    <g class="accent-dots" fill="#ffffff">
      <circle cx="811" cy="29" r="7"/>
      <circle cx="362" cy="102" r="7"/>
      <circle cx="818" cy="202" r="3"/>
      <circle cx="518" cy="215" r="4.5"/>
      <circle cx="664" cy="340" r="4.5"/>
      <circle cx="659" cy="357" r="2.5"/>
      <circle cx="440" cy="452" r="4"/>
      <circle cx="370" cy="539" r="6"/>
    </g>

    <circle cx="489" cy="339" r="78" fill="#ffffff"/>
    <circle class="food-photo" cx="489" cy="339" r="66" fill="url(#boardTone)" role="img" aria-label="Photograph of a charcuterie board with cured meats and cheese"/>

    <circle cx="157" cy="369" r="125" fill="#ffffff"/>
    <circle class="food-photo" cx="160" cy="371" r="112" fill="url(#pastaTone)" role="img" aria-label="Photograph of pappardelle in ragu topped with shaved cheese and microgreens"/>

    <circle cx="329" cy="333" r="105" fill="#ffffff"/>
    <circle class="food-photo" cx="331" cy="335" r="89" fill="url(#steakTone)" role="img" aria-label="Photograph of sliced roast meat with potatoes and microgreens"/>
  </svg>

  <div class="logo">
    <span class="logo-mark"></span>
    <span class="logo-name">Hearth<br>of the<br>Heron</span>
  </div>

  <h1 class="headline">Hearth of the Heron</h1>

  <p class="intro">Elegant comfort food that is upscale but simple.<br>Paired with an impressive wine selection and a<br>modern spin on classic cocktails.</p>

  <ul class="features">
    <li class="feature"><span>Open evenings with<br>a summer patio.</span>
      <svg width="16" height="16" viewBox="0 0 16 16" fill="none" stroke="#fff" stroke-width="1.6"><circle cx="7.5" cy="8.5" r="6"/><path d="M4.5 8.5 L7 11.5 L15 1.5"/></svg></li>
    <li class="feature"><span>Northern inspired<br>cuisine</span>
      <svg width="16" height="16" viewBox="0 0 16 16" fill="none" stroke="#fff" stroke-width="1.6"><circle cx="7.5" cy="8.5" r="6"/><path d="M4.5 8.5 L7 11.5 L15 1.5"/></svg></li>
  </ul>

  <p class="contact-label">CONTACT US</p>
  <p class="phone">867.555.0143</p>

  <div class="location">
    <div class="location-tab">LOCATED IN THE</div>
    <p class="address">Stonereach Hotel, 247 Larch Avenue.</p>
    <p class="website">www.hearthoftheheron-example.ca</p>
  </div>
</section>
</body>
</html>
```